This Project is listed for : Vexmoor only ... if you are not Vexmoors, please do not submit please

This is the listing for

Torbesca

business cards
very simple, elegant and firm
Black / Red / White

Target Market(s)

Adults
Investors
Clients

Industry/Entity Type

Business

Font styles to use
Decorative
Script

```html
<!DOCTYPE html>
<html lang="en">
<head>
<meta charset="utf-8">
<title>Torbesca — Business Cards</title>
<link rel="stylesheet" href="https://fonts.googleapis.com/css2?family=Courier+Prime:wght@400;700&family=Josefin+Sans:wght@400;600&display=swap">
<style>
  :root {
    --page: #e9e7e4;
    --card-black: #1e1e1f;
    --card-black-edge: #2a2a2b;
    --card-silver-light: #fbfbfb;
    --card-silver-mid: #e6e6e6;
    --edge-band: #d9d9d9;
    --ink-white: #f4f4f4;
    --ink-dark: #222222;
    --accent-red: #c9252b;
    --faint-mark: rgba(255, 255, 255, 0.06);
  }
  * { box-sizing: border-box; margin: 0; padding: 0; }
  html, body { width: 1200px; height: 900px; overflow: hidden; }
  body {
    background: var(--page);
    display: flex;
    flex-direction: column;
    align-items: center;
    justify-content: center;
    gap: 48px;
  }
  .card {
    position: relative;
    width: 660px;
    height: 377px;
    border-radius: 4px;
    overflow: hidden;
    box-shadow: 0 10px 28px rgba(0, 0, 0, 0.22);
  }

  /* Back side */
  .card-back {
    background: linear-gradient(100deg, var(--card-silver-light) 0%, var(--card-silver-mid) 45%, var(--card-silver-light) 70%, var(--card-silver-mid) 100%);
  }
  .edge-band {
    position: absolute;
    left: 0; right: 0;
    height: 40px;
    background: linear-gradient(180deg, var(--edge-band), var(--card-silver-mid));
  }
  .edge-band.top { top: 0; }
  .edge-band.bottom { bottom: 0; transform: scaleY(-1); }
  .back-brand {
    position: absolute;
    inset: 0;
    display: flex;
    flex-direction: column;
    align-items: center;
    justify-content: center;
    gap: 20px;
  }
  .brand-dot {
    width: 92px; height: 92px;
    border-radius: 50%;
    background: var(--ink-dark);
  }
  .back-brand .brand-name {
    font-family: "Courier Prime", "Courier New", monospace;
    font-size: 46px;
    color: var(--ink-dark);
    letter-spacing: 1px;
  }

  /* Front side */
  .card-front {
    background: linear-gradient(90deg, var(--card-black) 0%, var(--card-black-edge) 50%, var(--card-black) 100%);
    color: var(--ink-white);
  }
  .faint-mark {
    position: absolute;
    right: -40px; bottom: -70px;
    width: 290px; height: 290px;
    border-radius: 50%;
    background: var(--faint-mark);
  }
  .holder {
    position: absolute;
    left: 44px; top: 44px;
    font-family: "Josefin Sans", "Futura", sans-serif;
  }
  .holder-name {
    font-size: 22px;
    font-weight: 600;
    letter-spacing: 1px;
    text-transform: uppercase;
  }
  .holder-role {
    margin-top: 4px;
    font-size: 14px;
    color: var(--accent-red);
    letter-spacing: 3px;
    text-transform: uppercase;
  }
  .front-brand {
    position: absolute;
    right: 48px; top: 92px;
    font-family: "Courier Prime", "Courier New", monospace;
    font-size: 36px;
    letter-spacing: 1px;
  }
  .contact-list {
    position: absolute;
    left: 44px; top: 205px;
    list-style: none;
    font-family: "Josefin Sans", "Futura", sans-serif;
    font-size: 19px;
    letter-spacing: 0.5px;
  }
  .contact-list li {
    display: flex;
    align-items: center;
    gap: 14px;
    height: 34px;
  }
  .contact-icon { width: 18px; height: 18px; flex: none; }
  .contact-email, .contact-handle { text-transform: uppercase; }
</style>
</head>
<body>

  <section class="card card-back" aria-label="Business card, back">
    <div class="edge-band top" role="img" aria-label="Film-strip edge pattern along the top of the card"></div>
    <div class="back-brand">
      <span class="brand-dot"></span>
      <span class="brand-name">Torbesca</span>
    </div>
    <div class="edge-band bottom" role="img" aria-label="Film-strip edge pattern along the bottom of the card"></div>
  </section>

  <section class="card card-front" aria-label="Business card, front">
    <span class="faint-mark"></span>
    <div class="holder">
      <p class="holder-name">Mara Lenore Quillfield</p>
      <p class="holder-role">Producer, Artist, Executive</p>
    </div>
    <p class="front-brand">Torbesca</p>
    <ul class="contact-list">
      <li>
        <svg class="contact-icon" viewBox="0 0 18 18" aria-hidden="true">
          <rect x="4.5" y="1" width="9" height="16" rx="1.5" fill="none" stroke="var(--accent-red)" stroke-width="1.8"/>
          <line x1="7.5" y1="14" x2="10.5" y2="14" stroke="var(--accent-red)" stroke-width="1.6"/>
        </svg>
        <span class="contact-phone">+65 5550 0142</span>
      </li>
      <li>
        <svg class="contact-icon" viewBox="0 0 18 18" aria-hidden="true">
          <rect x="1" y="3.5" width="16" height="11" fill="var(--accent-red)"/>
          <polyline points="1,3.5 9,10 17,3.5" fill="none" stroke="var(--card-black)" stroke-width="1.4"/>
        </svg>
        <span class="contact-email">maralenore@inboxmail.net</span>
      </li>
      <li>
        <svg class="contact-icon" viewBox="0 0 18 18" aria-hidden="true">
          <rect x="3" y="3" width="12" height="12" fill="var(--accent-red)"/>
        </svg>
        <span class="contact-handle">@maralenore</span>
      </li>
    </ul>
  </section>

</body>
</html>
```